Cards/Stationary for program
Brightlanewords
Cards/Stationary for program - Education
Creative Brief
Bright & Fun-filled
Rachel Torvik
Licensed Clinical Social Worker
P.O Box 4067 Seabright, Or, 97452
brightlanewords@quellmail.com
Helping young people stay smart and safe online. would want another template to insert another co-workers name if possible

```html
<!DOCTYPE html>
<html lang="en">
<head>
<meta charset="utf-8">
<title>Brightlanewords – Business Card</title>
<link rel="stylesheet" href="https://fonts.googleapis.com/css2?family=Poppins:wght@400;600;700&display=swap">
<style>
  :root {
    --backdrop: #000000;
    --card: #fcfcfc;
    --ink: #1c1c1c;
    --ink-soft: #333333;
    --ink-name: #3a3a3a;
    --accent-red: #e5262b;
  }
  html, body {
    margin: 0;
    padding: 0;
    width: 1200px;
    height: 1016px;
    overflow: hidden;
    background: var(--backdrop);
    font-family: "Poppins", sans-serif;
  }
  .canvas {
    position: relative;
    width: 1200px;
    height: 1016px;
    background: var(--backdrop);
  }
  .business-card {
    position: absolute;
    left: 140px;
    top: 286px;
    width: 919px;
    height: 531px;
    background: var(--card);
    color: var(--ink);
  }
  .brand {
    position: absolute;
    left: 26px;
    top: 70px;
    width: 360px;
    text-align: center;
  }
  .brand-dot {
    display: block;
    width: 70px;
    height: 70px;
    margin: 0 auto 20px;
    border-radius: 50%;
    background: var(--accent-red);
  }
  .brand-name {
    margin: 0;
    font-size: 40px;
    font-weight: 700;
    letter-spacing: -0.5px;
    line-height: 1.1;
    color: var(--ink);
  }
  .tagline {
    margin: 99px 0 0;
    font-size: 23px;
    font-weight: 400;
    line-height: 1.22;
    color: var(--ink-soft);
  }
  .contact {
    position: absolute;
    right: 57px;
    top: 230px;
    text-align: right;
  }
  .contact-name {
    margin: 0;
    font-size: 38px;
    font-weight: 600;
    line-height: 1.1;
    color: var(--ink-name);
  }
  .contact-role {
    margin: 4px 0 0;
    font-size: 23px;
    font-weight: 400;
    line-height: 1.22;
    color: var(--ink-soft);
  }
  .contact-address {
    margin: 50px 0 0;
    font-style: normal;
    font-size: 23px;
    line-height: 1.4;
    color: var(--ink-soft);
  }
  .contact-email {
    margin: 16px 0 0;
    font-size: 23px;
    color: var(--ink-soft);
  }
</style>
</head>
<body>
<div class="canvas">
  <section class="business-card">
    <div class="brand">
      <span class="brand-dot"></span>
      <p class="brand-name">Brightlanewords</p>
      <p class="tagline">Helping young people stay<br>smart and safe online</p>
    </div>
    <div class="contact">
      <h1 class="contact-name">Rachel Torvik</h1>
      <p class="contact-role">Licensed Clinical Social Worker<br>#40213</p>
      <address class="contact-address">P.O Box 4067<br>Seabright, Or, 97452</address>
      <p class="contact-email">brightlanewords@quellmail.com</p>
    </div>
  </section>
</div>
</body>
</html>
```